Cruise price comparison web design project

The project's name is Seereisemöwe.
www.seereisemoewe-example.de
The current design (which I don't really like) can be found here:
http://srm02.seereisemoewe-example.de/

I m not too happy with what the current developers have been done so far (in terms of design), so I hope to find a great designer her to develop a design that kicks arses. : )

We are currently developing a site for the German market that brings travel agents and cruise holiday makers together. We are not an ordinary travel agency.
Seereisemöwe is a quick and convenient way to have independent travel agencies compete to offer our site visitors the best cruise deal available in Europe.

Here is a short video that explains what one of our competitors does; it gives a good overview as our site will be similar:
http://www.sailbidder-example.com/video_how_sailbidder_works.php
(Sailbidder-example.com is not a great website in terms of design, so please dont get me wrong.)

The logo has already been created, but both the colours (should remain blueish) and the font can be modified. The font colour can be changed dramatically if you think this is of advantage.

The Website design should be professional and unique and become an eye catcher. It must attract visitors of all age groups, a "wow-effect" is definitely a bonus.
Users should easily see what this website is about.

We need the following text on our homepage:

"Immer der beste Preis -
denn Reisebüros kämpfen um Sie!"
(means "Always the best rate - as travel agents compete offer the best deal")
This is a sort of headline.

We also need:

So funktioniert Seereisemöwe:
1. Wunschkreuzfahrt wählen
2. Angebote erhalten und vergleichen
3. Reisebüro kontaktieren und buchen

(This explains briefly how our system works.)

Aside banners maybe needed later for advertising.

Additions I need on the front page are:
- Login / Sign-Up / Your benefits
(I quite like the way it's done on http://www.harborherald-example.com, at the very top of the page)
- Recommendation-link
(for everything else: Pls. refer to srm02.seereisemoewe-example.de
- 3 or 4 "top offers of the week"
(current format is not very appealing; offers can be displayed as on http://voyages.tripvendo-example.com/affiliate/promo.rvlx?OfferID=XQLMOV27 or

A maritime look is surely an option here, as we focus on cruises. But maybe you can surprise me with a great idea.

I quite like the designs where basically one photo / picture is used.
Some examples which look great IMHO:
http://zed-works.artfolio-example.com/art/Coral-Lanterns-418305927
http://morvanpixels.artfolio-example.com/art/Website-Design-593017246
The following designer has also done a great job:
http://layoutsmith4836.artfolio-example.com/gallery/

ATTACHED:

Please get in touch with me if there are any questions or if you require further details. I ll get back to all inquiries / messages as soon as possible, usually within a few hours... Feel free to ask technical questions, too, (if any), the developer will be of assistance.
Updates

Reason: I decided to extend the deadline to have more time to comment on your designs and allow you to submit a few more proposals.

Reason: Sorry, more time needed to comment on all designs. Apart from this, some designers asked for more time.

Dear All,

Thank you so much for all your proposals.
Later today I will have a decent internet connection connection again, so I will be able to finally comment on your ideas and visions.

Hopefully next week we can finalize this project. Feel free to submit more designs or ask any questions if there are any.
Remember: Seereisemöwe won't be an ordinary travel agent. It brings cruise holiday makers and travel agents together.

Best

Target Market(s)

Holidaymakers / potential cruise holiday makers between 20 and 80.

Industry/Entity Type

Advertising

Requirements
Should not have
• Design should not use old-style, serif fonts.

```html
<!DOCTYPE html>
<html lang="de">
<head>
<meta charset="utf-8">
<title>Seereisemöwe – Kreuzfahrten im Preisvergleich</title>
<link rel="stylesheet" href="https://fonts.googleapis.com/css2?family=Fredoka:wght@500;600&family=Open+Sans:wght@400;600;700&family=Arimo:wght@400;700&display=swap">
<style>
:root{
  --bar-dark:#353535;
  --sky-top:#dfe6ee;
  --sky-bottom:#f4f6f9;
  --nav-blue:#2f5cae;
  --nav-blue-light:#4f7fd0;
  --navy:#1f3a78;
  --panel-navy:rgba(18,38,82,.78);
  --footer-dark:#2b2b2b;
  --footer-text:#b9b9b9;
  --white:#ffffff;
  --card-gray:#dcdcdc;
}
*{box-sizing:border-box;margin:0;padding:0}
html,body{width:1200px;height:960px;overflow:hidden}
body{position:relative;font-family:"Open Sans",Arial,sans-serif;background:#2a2a2a}
.abs{position:absolute}

.topbar{left:0;top:0;width:1200px;height:26px;background:var(--bar-dark);color:var(--white);font-family:Arimo,Arial,sans-serif;font-size:13px}
.topbar .links-left{left:127px;top:6px;word-spacing:2px}
.topbar .date{left:626px;top:6px;font-size:11px}
.topbar .links-right{left:884px;top:6px;word-spacing:2px}
.topbar .sep{margin:0 9px}

.header{left:0;top:26px;width:1200px;height:139px;background:linear-gradient(180deg,var(--sky-top),var(--sky-bottom) 60%,#e9eef4)}
.brand{left:132px;top:50px;display:flex;align-items:center;gap:10px}
.brand-mark{width:74px;height:74px;border-radius:50%;background:#3a64b3}
.brand-name{font-family:"Open Sans",sans-serif;font-weight:700;font-size:24px;color:#3a3a3a;letter-spacing:-.3px;white-space:nowrap}
.ad-slot{left:398px;top:51px;width:455px;height:71px;border:3px solid var(--white);box-shadow:0 0 3px rgba(0,0,0,.25);background:linear-gradient(90deg,#3b8fd8 0%,#1f6ec4 55%,#f2c216 76%,#f7cb20 100%)}
.connect{left:886px;top:38px;display:flex;align-items:center;gap:10px;font-family:"Fredoka",sans-serif;font-weight:600;font-size:20px;color:#3c3c3c}
.social{width:33px;height:33px;border-radius:6px;background:#cfd8e3;box-shadow:inset 0 0 0 1px #b7c2cf}
.search{left:885px;top:79px;width:204px;height:38px;border-radius:19px;background:linear-gradient(#e5e9ef,#f9fafc);box-shadow:inset 0 2px 3px rgba(0,0,0,.25),0 1px 0 #fff}
.search svg{position:absolute;right:9px;top:9px}
.adv-search{left:967px;top:121px;font-family:Arimo,sans-serif;font-weight:700;font-size:14px;color:#444;text-decoration:underline}

.nav{left:0;top:165px;width:1200px;height:35px;background:linear-gradient(180deg,var(--nav-blue-light),var(--nav-blue) 55%,#26509e);border-bottom:4px solid #bfcce3}
.nav ul{list-style:none;display:flex;position:absolute;left:128px;top:6px;height:29px}
.nav li{color:var(--white);font-size:13px;font-weight:600;padding:5px 0 0;position:relative;white-space:nowrap}
.nav li.active{background:linear-gradient(#fff,#e3e7ee);color:var(--navy);border-radius:4px 4px 0 0;padding:4px 11px 0}
.nav .dot{width:0;border-left:1px dotted #9fb6e0;height:22px;margin-top:2px}

.hero{left:0;top:204px;width:1200px;height:591px;background:linear-gradient(180deg,#2c5c96 0%,#1f4f8a 30%,#2d5a8a 55%,#8c96a0 72%,#b59a7c 85%,#9e7c5c 100%)}
.pitch{left:117px;top:231px;width:946px;height:229px;border:3px solid var(--white);border-radius:8px;background:var(--panel-navy);color:var(--white)}
.pitch h1{position:absolute;left:16px;top:10px;font-family:"Fredoka",sans-serif;font-weight:600;font-size:39px;line-height:47px;letter-spacing:.5px;text-shadow:0 0 2px #2850a8,0 0 3px #2850a8;white-space:nowrap}
.pitch h2{position:absolute;left:12px;top:112px;font-size:20px;font-weight:700}
.pitch ol{position:absolute;left:14px;top:145px;list-style:none;font-size:15px;font-weight:700;line-height:18px;letter-spacing:.3px}

.offer{top:530px;width:432px;height:232px;border:3px solid var(--white);border-radius:14px;background:linear-gradient(#f2f2f2,var(--card-gray));box-shadow:0 0 4px rgba(0,0,0,.3)}
.offer-title{position:absolute;left:8px;top:8px;width:410px;height:44px;border-radius:12px;background:linear-gradient(#fafafa,#d8d8d8);font-family:"Fredoka",sans-serif;font-weight:500;font-size:22px;color:var(--navy);padding:8px 0 0 11px;white-space:nowrap}
.offer-photo{position:absolute;left:22px;top:66px;width:157px;height:79px;background:linear-gradient(180deg,#9cc4e4,#4a86bb 60%,#2b4f74)}
.offer-photo span{position:absolute;left:8px;bottom:2px;color:#fff;font-size:13px;font-weight:600;text-shadow:0 1px 2px #000;white-space:nowrap}
.offer-lead{position:absolute;left:189px;top:72px;width:235px;font-size:12px;font-weight:700;color:#222;line-height:16px}
.offer-sub{position:absolute;font-family:Arimo,sans-serif;font-style:italic;font-size:12px;color:#333;line-height:14px}
.offer-date{position:absolute;right:20px;top:138px;font-family:Arimo,sans-serif;font-style:italic;font-weight:700;font-size:12px;color:#111}
.offer-rule{position:absolute;left:22px;top:153px;width:388px;border-top:1px solid #b5b5b5}
.price{position:absolute;left:28px;top:166px;font-family:Arimo,sans-serif;font-weight:700;font-size:22px;color:var(--navy)}
.per{position:absolute;left:104px;top:192px;font-family:Arimo,sans-serif;font-size:12px;font-weight:700;color:#222;text-decoration:underline;letter-spacing:.5px}
.order-btn{position:absolute;width:151px;height:38px;top:171px;border-radius:7px;background:linear-gradient(#666,#1b1b1b 55%,#000);border:1px solid #999;color:#fff;font-family:Arimo,sans-serif;font-weight:700;font-size:15px;letter-spacing:.4px;text-align:center;line-height:35px}

.footer{left:0;top:795px;width:1200px;height:137px;background:linear-gradient(#3a3a3a,var(--footer-dark));border-top:1px solid #555}
.fcol{top:12px;font-size:13px;color:var(--footer-text);line-height:15.5px}
.fcol h3{color:#e6e6e6;font-size:15px;font-weight:700;margin-bottom:11px}
.fdiv{top:10px;width:1px;height:117px;background:#5a5a5a}
.copyright{left:2px;top:932px;width:1198px;height:28px;background:#2a2a2a;color:#dcdcdc;font-size:12px;text-align:center;padding-top:5px}
</style>
</head>
<body>

<div class="abs topbar">
  <div class="abs links-left">Home<span class="sep">|</span>Help</div>
  <div class="abs date">20 Nov 2012 | 18:27 GMT+7</div>
  <div class="abs links-right">Login<span class="sep">|</span>Sign-Up<span class="sep">|</span>Your benefits</div>
</div>

<header class="abs header"></header>
<div class="abs brand">
  <div class="brand-mark"></div>
  <div class="brand-name">Seereisemöwe</div>
</div>
<div class="abs ad-slot" role="img" aria-label="Werbebanner von Hostwerk24: Reseller Webhosting, 24/7 Support, www.hostwerk24-example.info"></div>
<div class="abs connect">Connect us: <span class="social"></span><span class="social"></span></div>
<div class="abs search">
  <svg width="20" height="20" viewBox="0 0 20 20"><circle cx="8" cy="8" r="5.5" fill="none" stroke="#333" stroke-width="2"/><line x1="12" y1="12" x2="18" y2="18" stroke="#333" stroke-width="3" stroke-linecap="round"/></svg>
</div>
<div class="abs adv-search">Advanced Search</div>

<nav class="abs nav">
  <ul>
    <li class="active">Sun Gehts</li>
    <li style="width:20px"></li><li class="dot"></li><li style="width:27px"></li>
    <li>Receive</li>
    <li style="width:33px"></li><li class="dot"></li><li style="width:26px"></li>
    <li>Cruise Finder</li>
    <li style="width:30px"></li><li class="dot"></li><li style="width:28px"></li>
    <li>Shipping companies and vessels</li>
    <li style="width:29px"></li><li class="dot"></li><li style="width:29px"></li>
    <li>Specials</li>
    <li style="width:33px"></li><li class="dot"></li><li style="width:27px"></li>
    <li>Contact</li>
  </ul>
</nav>

<div class="abs hero" role="img" aria-label="Blick vom Bug eines Kreuzfahrtschiffs mit Holzdeck auf das offene blaue Meer"></div>

<section class="abs pitch">
  <h1>"Immer der beste Preis -denn Reisebüros<br>kämpfen um Sie!"</h1>
  <h2>So funktioniert Seereisemöwe:</h2>
  <ol>
    <li>1. Wunschkreuzfahrt wählen</li>
    <li>2. Angebote erhalten und vergleichen</li>
    <li>3. Reisebüro kontaktieren und buchen</li>
  </ol>
</section>

<article class="abs offer" style="left:123px">
  <div class="offer-title">Of the city of tango to the Big Apple</div>
  <div class="offer-photo" role="img" aria-label="Kreuzfahrtschiff auf See"><span>Aurora Meridian</span></div>
  <div class="offer-lead">Incl. Nordair flights, transfers and<br>hotel accom modation in Buenos Aires</div>
  <div class="offer-sub" style="left:192px;top:113px">22 days South America Cruise<br>Appointment</div>
  <div class="offer-date">in July 2012</div>
  <div class="offer-rule"></div>
  <div class="price">From € 2,899</div>
  <div class="per">Per person</div>
  <div class="order-btn" style="left:246px">Samples Order</div>
</article>

<article class="abs offer" style="left:596px">
  <div class="offer-title">Around Iceland - from / to Hamburg</div>
  <div class="offer-photo" role="img" aria-label="Pooldeck eines Kreuzfahrtschiffs" style="left:17px;background:linear-gradient(180deg,#bcd3e6,#6d9cc0 45%,#3d6d8f)"><span>Nordlicht Voyager</span></div>
  <div class="offer-lead" style="left:183px">Top Offer</div>
  <div class="offer-sub" style="left:183px;top:92px">12 days Iceland Cruise</div>
  <div class="offer-date">June 26, 2012</div>
  <div class="offer-rule" style="left:17px"></div>
  <div class="price" style="left:22px">From € 2,899</div>
  <div class="per" style="left:98px">Per person</div>
  <div class="order-btn" style="left:248px">Samples Order</div>
</article>

<footer class="abs footer">
  <div class="abs fcol" style="left:133px"><h3>About Us</h3>About Seereisemöwe.de<br>Jobs<br>Partner<br>Advertise Seereisemöwe.de</div>
  <div class="abs fdiv" style="left:358px"></div>
  <div class="abs fcol" style="left:398px"><h3>Press</h3>Press material<br>Seereisemöwe in the media<br>Press Releases<br>Seereisemöwe and the social<br>media</div>
  <div class="abs fdiv" style="left:605px"></div>
  <div class="abs fcol" style="left:648px"><h3>Help &amp; Service</h3>Product Reviews<br>Contact<br>FAQ's</div>
  <div class="abs fdiv" style="left:835px"></div>
  <div class="abs fcol" style="left:880px"><h3>Disclaimer</h3>Disclaimer / disclaimer<br>Terms of Service<br>Imprint</div>
</footer>
<div class="abs copyright">© 2010-2012 Seereisemöwe.de</div>

</body>
</html>
```